Business Card Design Harlow Airflow Systems

The Business will be centred around supply and installation of Ventilation for domestic homes and warehousing/workshops, and will be marketed as a Eco friendly means of reducing your carbon footprint and reducing energy consumption.Our suppliers will provide a range of products that will ventilate roof spaces and later will branch into to air transfer within homes for cooling and heating other rooms of the home etc.I would like to see colours that would be commensurate with the logo provided and yet not dominate the logo.Final design should convey a Diverse , professional but friendly service that will suit client needs

Target Market(s)

Domestic home owners and warehousing/workshop businesses

Industry/Entity Type

Business

Contact Information for Business Card

Company Name: Harlow Airflow Systems Pty Ltd, ABN: 42 817 350 294, Address: 27 Merrow Tunstead W.A 6084, Email: dale@harlowairflowsystems.com.au, Mobile Number: 0451 862 019

Requirements
Nice to have
• A tract art that commensurate of the logo supplied
Should not have
• Font style that opposes logo design

```html
<!DOCTYPE html>
<html lang="en">
<head>
<meta charset="utf-8">
<title>Harlow Airflow Systems – Business Card</title>
<link href="https://fonts.googleapis.com/css2?family=Lato:wght@400;700&display=swap" rel="stylesheet">
<style>
  :root {
    --backdrop: #3a332f;
    --card: #0d0d0d;
    --card-edge: #1b1b1b;
    --accent: #1fa84a;
    --text: #f2f2f2;
    --silver: #c9c9c9;
    --divider: #2a2a2a;
  }
  * { margin: 0; padding: 0; box-sizing: border-box; }
  html, body {
    width: 1200px;
    height: 844px;
    overflow: hidden;
    background: var(--backdrop);
    font-family: "Lato", sans-serif;
  }
  .stage {
    width: 1200px;
    height: 844px;
    display: flex;
    align-items: center;
    justify-content: center;
    gap: 60px;
  }
  .card {
    width: 525px;
    height: 300px;
    background: radial-gradient(circle at 60% 35%, #1a1a1a 0%, var(--card) 70%);
    border: 1px solid var(--card-edge);
    border-radius: 4px;
    box-shadow: 0 14px 30px rgba(0, 0, 0, 0.55);
    position: relative;
  }
  .card-front {
    display: flex;
    align-items: center;
  }
  .brand-block {
    width: 250px;
    height: 100%;
    display: flex;
    align-items: center;
    justify-content: center;
  }
  .brand-name {
    font-weight: 700;
    font-size: 19px;
    color: var(--accent);
    display: flex;
    align-items: center;
    gap: 8px;
  }
  .brand-mark {
    width: 12px;
    height: 12px;
    background: currentColor;
    display: inline-block;
  }
  .divider {
    width: 1px;
    height: 200px;
    background: var(--divider);
  }
  .contact-block {
    padding-left: 26px;
    color: var(--text);
    font-size: 14px;
    line-height: 1.35;
  }
  .person-name {
    color: var(--accent);
    font-size: 21px;
    font-weight: 700;
    line-height: 1.1;
  }
  .person-role { margin-bottom: 14px; }
  .address { margin-bottom: 14px; }
  .contact-line .label {
    color: var(--accent);
    display: inline-block;
    width: 16px;
  }
  .card-back {
    display: flex;
    align-items: center;
    justify-content: center;
  }
  .card-back .brand-name {
    color: var(--silver);
    font-size: 30px;
    gap: 12px;
  }
  .card-back .brand-mark {
    width: 16px;
    height: 16px;
  }
</style>
</head>
<body>
  <main class="stage">
    <section class="card card-front" aria-label="Business card front">
      <div class="brand-block">
        <div class="brand-name"><span class="brand-mark"></span>Harlow Airflow Systems</div>
      </div>
      <div class="divider"></div>
      <div class="contact-block">
        <div class="person-name">Dale Marsh</div>
        <div class="person-role">Managing Director</div>
        <div class="address">27 Merrow Tunstead<br>W.A 6084</div>
        <div class="contact-line"><span class="label">T:</span> 0451 862 019</div>
        <div class="contact-line"><span class="label">E:</span> dale@harlowairflowsystems.com.au</div>
        <div class="contact-line"><span class="label">W:</span>www.harlowairflow.com.au</div>
      </div>
    </section>
    <section class="card card-back" aria-label="Business card back">
      <div class="brand-name"><span class="brand-mark"></span>Harlow Airflow Systems</div>
    </section>
  </main>
</body>
</html>
```